Digital multi-page Product Brochure

We’re creating a product brochure for our Wood Look Porcelain Pavers. The brochure will show technical details of the pavers, available colors, and applications while also showcasing the advantages of porcelain over wood.
We prefer a clean design aesthetic with appropriate white space incorporated. Because we want the view to appreciate the detail and natural look of the porcelain pavers, we want relatively large color swatches in the available colors section.
Each color swatch section needs the information provided in the guide. The design and layout of these sections is completely open. We do want to see a visual of the paver size in each color swatch section along with the written sizing information.
Mixed use of renderings and actual installation photos. Style and placement of photos is up to designer.
Architects and contractors
Building Materials
- Outfit - headers, Helvetica for paragraph copy

```html
<!DOCTYPE html>
<html lang="en">
<head>
<meta charset="utf-8">
<title>Wood-Look Porcelain Pavers Brochure</title>
<link rel="stylesheet" href="https://fonts.googleapis.com/css2?family=Outfit:wght@400;500;700&family=Arimo:wght@400;700&display=swap">
<style>
:root{
  --board:#2b2b2b;
  --ink-dark:#222222;
  --teal:#0a7a83;
  --white:#ffffff;
  --copy:#5f6366;
  --soft:#e6eef0;
  --header-font:"Outfit",sans-serif;
  --body-font:"Arimo",Helvetica,sans-serif;
}
*{margin:0;padding:0;box-sizing:border-box}
html,body{width:1200px;height:1019px;overflow:hidden;background:var(--board)}
.board{position:relative;width:1200px;height:1019px}
.page{position:absolute;width:347px;height:448px;overflow:hidden;background:var(--white);font-family:var(--body-font);color:var(--copy)}
.abs{position:absolute}
.page-header{position:absolute;left:0;top:0;width:347px;height:51px}
.page-header h2{position:absolute;left:26px;top:0;height:44px;display:flex;align-items:center;font-family:var(--header-font);font-weight:400;color:var(--white);letter-spacing:.3px}
.page-footer{position:absolute;left:0;bottom:0;width:347px;height:34px}
.page-footer .copyright{position:absolute;left:26px;bottom:4px;font-size:4px;color:var(--white)}
.page-footer .page-num{position:absolute;left:269px;top:10px;font-size:8.6px;font-weight:700;color:var(--white)}
.photo{position:absolute}

/* cover */
.cover{left:47px;top:46px;background:var(--ink-dark)}
.cover h1{position:absolute;left:26px;top:340px;font-family:var(--header-font);font-weight:700;font-size:21.5px;line-height:30px;color:var(--white);letter-spacing:-.2px}

/* contents */
.contents{left:427px;top:46px}
.contents h2{font-size:23px}
.toc{position:absolute;left:26px;top:76px;list-style:none}
.toc li{font-size:11.5px;height:29.3px;line-height:16px;color:var(--copy)}

/* feature */
.feature{left:807px;top:46px}
.feature-card{position:absolute;left:133px;top:200px;width:186px;height:221px;background:var(--white)}
.feature-card h3{position:absolute;left:16px;top:8px;font-family:var(--header-font);font-weight:500;font-size:17px;color:var(--teal);letter-spacing:.3px}
.feature-panel{position:absolute;left:17px;top:36px;width:168px;height:168px;background:var(--teal);color:var(--white);font-size:8.1px;line-height:16.2px;padding:9px 8px 0 16px}
.feature-panel hr{border:0;border-top:.6px solid rgba(255,255,255,.55);margin:10px 0 6px}
.feature-panel p.short{line-height:14.5px}

/* advantage */
.advantage{left:47px;top:525px}
.advantage h2{font-size:14px}
.intro{position:absolute;left:26px;top:64px;width:300px;font-size:7.2px;line-height:13.9px}
.vs-title{position:absolute;left:26px;top:264px;font-size:9px;font-weight:700;color:var(--teal)}
.compare{position:absolute;left:27px;top:283px;width:201px;height:141px;background:var(--white);border-radius:3px;box-shadow:0 0 6px rgba(0,0,0,.1)}
.compare table{position:absolute;left:16px;top:4px;border-collapse:collapse;font-size:5px;color:var(--copy)}
.compare th{font-weight:700;font-size:4.4px;color:#333;height:11px;text-align:center}
.compare td{height:12.2px}
.compare td.mark{text-align:center;width:48px}
.compare td.label{width:89px}
.tick{width:6px;height:5px;display:inline-block;vertical-align:middle}

/* dimensions */
.dimensions{left:427px;top:525px}
.dimensions h2{font-size:14px}
.dimensions h3{position:absolute;left:26px;font-family:var(--header-font);font-weight:400;font-size:10px;color:#222}
.dimensions p{position:absolute;left:26px;font-size:7.2px;line-height:14px;white-space:nowrap}
.dimensions p.variation{font-size:6.9px;line-height:13.8px}
.label-teal{position:absolute;font-size:7.4px;font-weight:700;color:var(--teal)}
.size-box{position:absolute;background:var(--soft);font-size:7.2px;color:var(--copy);display:flex;align-items:center;justify-content:center}
.swatch{position:absolute;width:28px;height:26px}
.swatch-label{position:absolute;top:422px;font-size:4.6px;color:#333}
.key{position:absolute;left:134px;top:392px;font-size:5.8px;line-height:11px}
</style>
</head>
<body>
<div class="board">

  <section class="page cover">
    <div class="photo" style="left:0;top:0;width:320px;height:322px;background:linear-gradient(160deg,#3b3a38 0%,#6a6560 45%,#8a8176 75%,#4a4640 100%)" role="img" aria-label="Glass-walled rooftop restaurant with wood tables and bentwood chairs on wood-look porcelain floor"></div>
    <div class="abs" style="left:320px;top:205px;width:27px;height:167px;background:var(--teal)"></div>
    <div class="abs" style="left:177px;top:322px;width:170px;height:50px;background:var(--teal)"></div>
    <h1>EVERYTHING YOU NEED TO<br>KNOW ABOUT WOOD-LOOK<br>PORCELAIN PAVERS</h1>
  </section>

  <section class="page contents">
    <svg class="page-header" viewBox="0 0 347 51"><rect width="347" height="51" fill="var(--teal)"/><polygon points="308,0 347,0 347,44 277,44" fill="var(--white)"/></svg>
    <div class="page-header"><h2>CONTENTS:</h2></div>
    <ol class="toc">
      <li>i. Advantages over Wood</li>
      <li>ii. Colors and Styles</li>
      <li>iii. Paver Sizes and Dimensions</li>
      <li>iv. Applications</li>
      <li>v. Installation</li>
      <li>vi. Laying Options</li>
      <li>vii. Project Inspiration</li>
    </ol>
    <div class="page-footer">
      <svg class="abs" style="left:0;top:0" width="347" height="34" viewBox="0 0 347 34"><polygon points="0,19 251,19 245,34 0,34" fill="var(--teal)"/><polygon points="250,0 347,0 347,34 238,34" fill="var(--ink-dark)"/></svg>
      <span class="copyright">(C) Copyright I All Rights Reserved</span>
      <span class="page-num">Page 02 Of 05</span>
    </div>
  </section>

  <section class="page feature">
    <div class="photo" style="left:0;top:0;width:347px;height:448px;background:linear-gradient(180deg,#cdb89a 0%,#b9a284 28%,#5a9aa0 45%,#c9a58c 65%,#b0886a 100%)" role="img" aria-label="Covered rooftop event terrace with string lights, pink-draped tables and gold chairs on wood-look pavers"></div>
    <div class="feature-card">
      <h3>NONCOMBUSTIBLE</h3>
      <div class="feature-panel">
        <p>Wood look porcelain pavers used with our Ember Steel Pedestals combine to create a 100% Fireproof decking installation. Fire codes and city requirements are frequently changing.</p>
        <hr>
        <p class="short">Our elevated decking system is<br>Class A fire rated.</p>
      </div>
    </div>
  </section>

  <section class="page advantage">
    <svg class="page-header" viewBox="0 0 347 51"><rect width="347" height="51" fill="var(--teal)"/><polygon points="308,0 347,0 347,44 277,44" fill="var(--white)"/></svg>
    <div class="page-header"><h2>THE PORCELAIN ADVANTAGE:</h2></div>
    <p class="intro">Terradeck Wood-Look Porcelain Pavers and Planks beautifully incorporate all the features that make natural wood so appealing, while eliminating the challenges and drawbacks of using wood or composite wood for various projects and installations.</p>
    <div class="abs" style="left:249px;top:190px;width:98px;height:83px;background:#333"></div>
    <div class="photo" style="left:26px;top:117px;width:294px;height:138px;background:linear-gradient(180deg,#6e4a3a 0%,#8a7560 40%,#b8b4aa 62%,#7a5438 82%,#5a3a26 100%);box-shadow:0 2px 6px rgba(0,0,0,.2)" role="img" aria-label="Courtyard patio with lounge seating and fountain on wood-look porcelain pavers between brick buildings"></div>
    <div class="photo" style="left:249px;top:288px;width:98px;height:118px;background:var(--teal)" role="img" aria-label="Teal-toned rooftop terrace installation photo"></div>
    <div class="vs-title">Wood-look Porcelain Pavers vs. Wood</div>
    <div class="compare">
      <table>
        <thead><tr><th></th><th>WOOD-LOOK PAVERS</th><th>WOOD</th></tr></thead>
        <tbody>
          <tr><td class="label">Stays cool in the sun</td><td class="mark">X</td><td class="mark"><svg class="tick" viewBox="0 0 6 5"><path d="M.6 2.6 2.3 4.2 5.4.8" fill="none" stroke="var(--teal)" stroke-width="1.2"/></svg></td></tr>
          <tr><td class="label">100% water resistant</td><td class="mark">X</td><td class="mark"><svg class="tick" viewBox="0 0 6 5"><path d="M.6 2.6 2.3 4.2 5.4.8" fill="none" stroke="var(--teal)" stroke-width="1.2"/></svg></td></tr>
          <tr><td class="label">Scratch resistant</td><td class="mark">X</td><td class="mark"><svg class="tick" viewBox="0 0 6 5"><path d="M.6 2.6 2.3 4.2 5.4.8" fill="none" stroke="var(--teal)" stroke-width="1.2"/></svg></td></tr>
          <tr><td class="label">Fireproof</td><td class="mark">X</td><td class="mark"><svg class="tick" viewBox="0 0 6 5"><path d="M.6 2.6 2.3 4.2 5.4.8" fill="none" stroke="var(--teal)" stroke-width="1.2"/></svg></td></tr>
          <tr><td class="label">Low Maintenance</td><td class="mark">X</td><td class="mark"><svg class="tick" viewBox="0 0 6 5"><path d="M.6 2.6 2.3 4.2 5.4.8" fill="none" stroke="var(--teal)" stroke-width="1.2"/></svg></td></tr>
          <tr><td class="label">Fade resistant</td><td class="mark">X</td><td class="mark"><svg class="tick" viewBox="0 0 6 5"><path d="M.6 2.6 2.3 4.2 5.4.8" fill="none" stroke="var(--teal)" stroke-width="1.2"/></svg></td></tr>
          <tr><td class="label">Cold resistant (won't warp or twist)</td><td class="mark">X</td><td class="mark"><svg class="tick" viewBox="0 0 6 5"><path d="M.6 2.6 2.3 4.2 5.4.8" fill="none" stroke="var(--teal)" stroke-width="1.2"/></svg></td></tr>
          <tr><td class="label">On-grade or pedestal supported</td><td class="mark">X</td><td class="mark"><svg class="tick" viewBox="0 0 6 5"><path d="M.6 2.6 2.3 4.2 5.4.8" fill="none" stroke="var(--teal)" stroke-width="1.2"/></svg></td></tr>
          <tr><td class="label">Slip resistant</td><td class="mark">X</td><td class="mark"><svg class="tick" viewBox="0 0 6 5"><path d="M.6 2.6 2.3 4.2 5.4.8" fill="none" stroke="var(--teal)" stroke-width="1.2"/></svg></td></tr>
          <tr><td class="label">Insect resistant</td><td class="mark">X</td><td class="mark"><svg class="tick" viewBox="0 0 6 5"><path d="M.6 2.6 2.3 4.2 5.4.8" fill="none" stroke="var(--teal)" stroke-width="1.2"/></svg></td></tr>
        </tbody>
      </table>
    </div>
    <div class="page-footer">
      <svg class="abs" style="left:0;top:0" width="347" height="34" viewBox="0 0 347 34"><polygon points="0,19 251,19 245,34 0,34" fill="var(--teal)"/><polygon points="250,0 347,0 347,34 238,34" fill="var(--ink-dark)"/></svg>
      <span class="copyright">(C) Copyright I All Rights Reserved</span>
      <span class="page-num">Page 04 Of 05</span>
    </div>
  </section>

  <section class="page dimensions">
    <svg class="page-header" viewBox="0 0 347 51"><rect width="347" height="51" fill="var(--teal)"/><polygon points="308,0 347,0 347,44 277,44" fill="var(--white)"/></svg>
    <div class="page-header"><h2>DIMENSIONS AND FEATURES:</h2></div>
    <h3 style="top:61px">DIMENSIONS</h3>
    <p style="top:80px">*** This is simply informational, need a good way to display.</p>
    <p style="top:100px">Slabs 24” x 48”, 24” x 24”</p>
    <p style="top:115px">Planks 16” x 48”, 12” x 48”, 8” x 48”</p>
    <span class="label-teal" style="left:26px;top:141px">Slabs</span>
    <span class="label-teal" style="left:131px;top:141px">Planks</span>
    <div class="size-box" style="left:26px;top:157px;width:38px;height:38px">24*24</div>
    <div class="size-box" style="left:26px;top:205px;width:76px;height:37px">24*48</div>
    <div class="size-box" style="left:131px;top:157px;width:118px;height:22px">8*48</div>
    <div class="size-box" style="left:131px;top:184px;width:118px;height:24px">12*48</div>
    <div class="size-box" style="left:131px;top:216px;width:118px;height:29px">16*48</div>
    <div class="size-box" style="left:131px;top:254px;width:189px;height:24px">10 1/2” * 72”</div>
    <p style="top:292px">*** nominal sizes may vary by manufacturer. Confirm sizes with Terradeck before ordering.</p>
    <h3 style="top:314px">VARIATION</h3>
    <p class="variation" style="top:330px">Slight tone variations are inherent in porcelain pavers, slabs, and planks. Some colors and styles<br>have minimal variations between each paver and others are significantly distinct from one another.<br>(If we can't pull these from a catalog, we may need to replicate and create our own.)</p>
    <h3 style="top:377px">EXAMPLES FOR KEY</h3>
    <svg class="swatch" style="left:27px;top:394px" viewBox="0 0 28 26"><rect width="28" height="26" fill="#eee"/><rect x="2" y="2" width="7" height="6.5" fill="#999"/><rect x="10.5" y="2" width="7" height="6.5" fill="#aaa"/><rect x="19" y="2" width="7" height="6.5" fill="#b5b5b5"/><rect x="2" y="10" width="7" height="6.5" fill="#aaa"/><rect x="10.5" y="10" width="7" height="6.5" fill="#a0a0a0"/><rect x="19" y="10" width="7" height="6.5" fill="#999"/><rect x="2" y="18" width="7" height="6.5" fill="#b0b0b0"/><rect x="10.5" y="18" width="7" height="6.5" fill="#999"/><rect x="19" y="18" width="7" height="6.5" fill="#a5a5a5"/></svg>
    <svg class="swatch" style="left:64px;top:394px" viewBox="0 0 28 26"><rect width="28" height="26" fill="#eee"/><rect x="2" y="2" width="7" height="6.5" fill="#777"/><rect x="10.5" y="2" width="7" height="6.5" fill="#aaa"/><rect x="19" y="2" width="7" height="6.5" fill="#888"/><rect x="2" y="10" width="7" height="6.5" fill="#aaa"/><rect x="10.5" y="10" width="7" height="6.5" fill="#666"/><rect x="19" y="10" width="7" height="6.5" fill="#999"/><rect x="2" y="18" width="7" height="6.5" fill="#888"/><rect x="10.5" y="18" width="7" height="6.5" fill="#bbb"/><rect x="19" y="18" width="7" height="6.5" fill="#777"/></svg>
    <svg class="swatch" style="left:97px;top:394px" viewBox="0 0 28 26"><rect width="28" height="26" fill="#eee"/><rect x="2" y="2" width="7" height="6.5" fill="#333"/><rect x="10.5" y="2" width="7" height="6.5" fill="#ccc"/><rect x="19" y="2" width="7" height="6.5" fill="#777"/><rect x="2" y="10" width="7" height="6.5" fill="#222"/><rect x="10.5" y="10" width="7" height="6.5" fill="#999"/><rect x="19" y="10" width="7" height="6.5" fill="#ddd"/><rect x="2" y="18" width="7" height="6.5" fill="#aaa"/><rect x="10.5" y="18" width="7" height="6.5" fill="#222"/><rect x="19" y="18" width="7" height="6.5" fill="#888"/></svg>
    <span class="swatch-label" style="left:27px">V2</span>
    <span class="swatch-label" style="left:65px">V3</span>
    <span class="swatch-label" style="left:97px">V4</span>
    <div class="key">V2 – minimal variation<br>V3 – moderate variation<br>V4 – significant variation</div>
    <div class="page-footer">
      <svg class="abs" style="left:0;top:0" width="347" height="34" viewBox="0 0 347 34"><polygon points="0,19 251,19 245,34 0,34" fill="var(--teal)"/><polygon points="250,0 347,0 347,34 238,34" fill="var(--ink-dark)"/></svg>
      <span class="copyright">(C) Copyright I All Rights Reserved</span>
      <span class="page-num">Page 05 Of 05</span>
    </div>
  </section>

</div>
</body>
</html>
```